Business Card Design Project

Business card design for an IT Service company. A logo has already been created in a different contest and has been attached to this project. Ideally we're looking for a double sided business card that matches the look and feel of our newly created logo.

We're open to creativity if you feel a tag line is needed such as "IT Services and Application Development". We're open to really and look and feel - even single sided business cards if you feel you have something that's a great idea.

Last thought here - I'm not sure how it'll look but maybe a two tone card? One side dark blue and the other side white? Don't limit the design submissions to this tho - just curious if it would look good

Nothing too busy please - simple... Thank you and happy designing!

Target Market(s)

Businesses that require IT Services and support for hosted services, technical consultation, web design.

Industry/Entity Type

Business

Font styles to use
Sans Serif

Requirements
Must have
• Use the colors provided in the logo (see attachment) or additional colors that compliment
Must have the following contact info (not necessarily in this order):
- Alan Fisk
- Founding Partner
- afisk@quillbarrow.example
- 555-382-1946
- www.quillbarrow.example

```html
<!DOCTYPE html>
<html lang="en">
<head>
<meta charset="utf-8">
<title>Quillbarrow Business Card</title>
<link rel="stylesheet" href="https://fonts.googleapis.com/css2?family=Arimo:wght@400;700&display=swap">
<style>
  :root {
    --backdrop: #d9d9d7;
    --card-yellow: #f6ef4a;
    --brand-navy: #1d2a5e;
    --brand-green: #5a9a3a;
    --card-blue: #2a2f96;
    --card-blue-light: #1c5ab4;
    --card-text: #ffffff;
  }
  * { box-sizing: border-box; margin: 0; padding: 0; }
  html, body {
    width: 1179px;
    height: 1200px;
    overflow: hidden;
    background: var(--backdrop);
    font-family: "Arimo", Arial, sans-serif;
  }
  .sheet {
    width: 1179px;
    height: 1200px;
    display: flex;
    flex-direction: column;
    align-items: center;
    justify-content: center;
    gap: 44px;
  }
  .card {
    position: relative;
    width: 900px;
    height: 514px;
    overflow: hidden;
    box-shadow: 0 6px 18px rgba(0, 0, 0, 0.18);
  }
  .card--front {
    background: var(--card-yellow);
    display: flex;
    align-items: center;
    justify-content: center;
  }
  .brand {
    display: flex;
    align-items: center;
    gap: 22px;
  }
  .brand__mark {
    width: 40px;
    height: 40px;
    border-radius: 50%;
    background: var(--brand-green);
  }
  .brand__name {
    font-weight: 700;
    font-size: 86px;
    letter-spacing: 1px;
    color: var(--brand-navy);
  }
  .card--back {
    background: var(--card-blue);
  }
  .card__waves {
    position: absolute;
    inset: 0;
    width: 100%;
    height: 100%;
  }
  .contact {
    position: absolute;
    left: 0;
    right: 0;
    top: 220px;
    text-align: center;
    color: var(--card-text);
  }
  .contact__name {
    font-weight: 700;
    font-size: 34px;
  }
  .contact__role {
    font-size: 22px;
    letter-spacing: 14px;
    margin: 4px 0 14px;
    padding-left: 14px;
  }
  .contact__email,
  .contact__web {
    font-size: 30px;
  }
  .contact__phone {
    font-weight: 700;
    font-size: 32px;
    margin: 6px 0;
  }
</style>
</head>
<body>
  <main class="sheet">
    <section class="card card--front">
      <div class="brand">
        <span class="brand__mark"></span>
        <span class="brand__name">Quillbarrow</span>
      </div>
    </section>

    <section class="card card--back">
      <svg class="card__waves" viewBox="0 0 900 514" preserveAspectRatio="none" role="img" aria-label="Flowing blue line-wave background pattern">
        <defs>
          <linearGradient id="waveGlow" x1="0" y1="0" x2="1" y2="1">
            <stop offset="0" stop-color="#2a2f96"/>
            <stop offset="0.45" stop-color="#1c5ab4"/>
            <stop offset="1" stop-color="#2a2f96"/>
          </linearGradient>
        </defs>
        <rect width="900" height="514" fill="url(#waveGlow)" opacity="0.55"/>
      </svg>
      <div class="contact">
        <p class="contact__name">Alan Fisk</p>
        <p class="contact__role">Founding Partner</p>
        <p class="contact__email">afisk@quillbarrow.example</p>
        <p class="contact__phone">555-382-1946</p>
        <p class="contact__web">www.quillbarrow.example</p>
      </div>
    </section>
  </main>
</body>
</html>
```